I challenge you to create Denmark's coolest roofing company website

We need to have a website created for our roofing company.

I have some pages that can be used as a starting point because there are some things we would like to have, one important thing is a roof calculator, in addition to that information about the company, pictures of tasks we have completed, links to Friendlio and Pictavoro pages.

reviews from rated, etc. should also be visible on the page.

we have lots of pictures, videos, logos,

we need to have a nice home page that is just a little cooler than the competitors.
we need to steal their customer. the page should be easy and clear but with a nice design.
an important thing is the calculator.
come up with some suggestions we are quite open as long as it is a nice design
Updates

I have made an update in the PDF file with some thoughts and wishes. The file has been uploaded.

Target Market(s)

20-60

Industry/Entity Type

carpenter - roofer

Coding

Coded - Design and coding required

Number of Pages Required

4 page

Font styles to use
Sans Serif

Colors
EB3D1F
EC4F4E
F09395
F8D3D4
FCEDEE

Requirements
Must have
• Roof calculator, nice design, easy to get around
Nice to have
• the competitors : https://mollerbyghuset.dk https://hvid-tegl.dk https://strandbyghuset.dk

```html
<!DOCTYPE html>
<html lang="en">
<head>
<meta charset="utf-8">
<title>Roofing Company – Home</title>
<link href="https://fonts.googleapis.com/css2?family=Poppins:wght@400;500;600;700&family=Russo+One&display=swap" rel="stylesheet">
<style>
:root{
  --red:#EB3D1F;
  --red-soft:#EC4F4E;
  --pink:#F09395;
  --blush:#F8D3D4;
  --cream:#FCEDEE;
  --ink:#111111;
  --text:#333333;
  --muted:#666666;
  --line:#e6e6e6;
  --field:#f1f1f1;
  --white:#ffffff;
}
*{box-sizing:border-box;margin:0;padding:0}
html,body{width:1200px;height:4295px;overflow:hidden}
body{position:relative;background:var(--white);font-family:"Poppins",sans-serif;color:var(--text)}
.display{font-family:"Russo One",sans-serif;text-transform:uppercase;color:var(--ink);letter-spacing:.3px;font-weight:400}
.abs{position:absolute}
svg{display:block}

/* top bar */
.topbar{left:0;top:0;width:1200px;height:34px;background:var(--ink);color:#fff;font-size:11px;display:flex;align-items:center;padding:0 88px}
.topbar .item{display:flex;align-items:center;gap:7px;margin-right:30px}
.topbar .social{margin-left:auto;display:flex;gap:16px;font-size:10px;font-weight:500}

/* hero */
.hero{left:0;top:34px;width:1200px;height:753px;background:linear-gradient(160deg,#8d99a6 0%,#5b6470 30%,#2c2f35 60%,#1e1f23 100%)}
.hero-shade{left:0;top:0;width:1200px;height:753px;background:linear-gradient(90deg,rgba(0,0,0,.35),rgba(0,0,0,0) 60%)}
.logo{font-family:"Russo One",sans-serif;font-size:28px;color:#fff}
.nav{left:433px;top:26px;display:flex;gap:22px;font-size:11px;font-weight:500;color:#fff}
.nav .active{color:var(--red)}
.btn{display:inline-flex;align-items:center;justify-content:center;font-size:11.5px;font-weight:500;color:#fff;background:var(--red);text-transform:uppercase}
.quote-btn{left:955px;top:14px;width:155px;height:38px}
.hero h1{left:88px;top:292px;font-size:39px;line-height:53px;color:#fff}
.hero .lede{left:90px;top:408px;font-size:13px;color:#fff}
.hero .btn-est{left:90px;top:447px;width:180px;height:40px}
.hero .btn-proj{left:280px;top:447px;width:168px;height:40px;background:transparent;border:1.5px solid #fff}

/* calculator */
.calc h2{left:130px;top:884px;font-size:25px;line-height:34px}
.calc p{left:130px;top:960px;font-size:12px;line-height:19px;color:var(--text);width:440px}
.field{height:35px;background:var(--field);font-size:9.5px;color:var(--muted);display:flex;align-items:center;padding:0 20px;justify-content:space-between}
.calc-btn{left:685px;top:971px;width:387px;height:36px;font-size:10px}

/* why */
.why-block{left:88px;top:1083px;width:232px;height:193px;background:var(--red)}
.why-photo{left:130px;top:1118px;width:452px;height:485px;background:linear-gradient(170deg,#7fa8d6 0%,#bcd3ea 45%,#4a4d55 75%,#2c2d33 100%)}
.why-panel{left:538px;top:1195px;width:534px;height:445px;background:var(--red);color:#fff}
.why-panel h2{position:absolute;left:90px;top:100px;font-size:25.5px;line-height:34px;color:#fff}
.why-panel p{position:absolute;left:90px;top:175px;width:400px;font-size:12px;line-height:19.5px}
.why-panel ul{position:absolute;left:90px;top:272px;list-style:none;font-size:11.5px;line-height:25.5px}
.why-panel li::before{content:"";display:inline-block;width:6px;height:6px;background:#fff;transform:rotate(45deg);margin-right:9px;vertical-align:2px}
.why-panel b{font-weight:600}

/* services */
.section-title{left:0;width:1200px;text-align:center;font-size:25px}
.service{top:1782px;width:300px;height:392px;display:flex;align-items:flex-end;padding:0 0 38px 38px;font-family:"Russo One",sans-serif;font-size:10.5px;color:#fff;text-transform:uppercase}

/* testimonials */
.testi h2{left:218px;top:2330px;font-size:25px}
.testi p{left:218px;top:2367px;width:340px;font-size:12px;line-height:19px}
.arrow-btn{top:2430px;width:46px;height:46px;display:flex;align-items:center;justify-content:center}
.review{left:662px;top:2267px;width:318px;height:297px;background:linear-gradient(135deg,#f6efe9,#e8ddd0);box-shadow:0 10px 30px rgba(0,0,0,.08)}
.review .text{position:absolute;left:20px;top:110px;width:260px;font-size:12px;line-height:20px;color:#555}
.review .name{position:absolute;left:25px;top:218px;font-size:15px}
.review .stars{position:absolute;left:183px;top:220px;display:flex;gap:3px}

/* projects */
.proj{background:linear-gradient(160deg,#9bb0c4,#6b7a86 60%,#4a5660)}
.link-badge{left:768px;top:2965px;width:76px;height:76px;border-radius:50%;background:#fff;display:flex;align-items:center;justify-content:center}

/* contact */
.contact h2{left:213px;top:3510px;font-size:25px}
.contact p{left:213px;top:3553px;width:370px;font-size:12px;line-height:20px}
.ci{left:213px;width:52px;height:52px;background:var(--red);display:flex;align-items:center;justify-content:center}
.ci-label{left:278px;font-size:10px;font-family:"Russo One",sans-serif;color:var(--ink)}
.ci-value{left:278px;font-size:20px;font-family:"Russo One",sans-serif;color:var(--ink)}
.form-box{left:635px;top:3403px;width:364px;height:400px;background:var(--red);box-shadow:0 10px 30px rgba(0,0,0,.12)}
.input{position:absolute;left:38px;width:288px;height:43px;background:#fff;font-size:8.5px;color:#999;padding:14px 22px}
.submit{position:absolute;left:38px;top:318px;width:288px;height:37px;background:var(--ink);color:#fff;font-size:10px;font-weight:500;display:flex;align-items:center;justify-content:center;text-transform:uppercase}

/* footer */
.footer{left:0;top:3903px;width:1200px;height:392px;background:var(--ink);color:#fff}
.footer .flogo{position:absolute;left:117px;top:155px;font-family:"Russo One",sans-serif;font-size:32px;color:var(--red)}
.fcol{position:absolute;top:95px}
.fcol h4{font-family:"Russo One",sans-serif;font-size:13.5px;color:var(--red);text-transform:uppercase;line-height:21px;font-weight:400;margin-bottom:8px}
.fcol a{display:block;font-size:12px;line-height:26.5px;color:#fff;text-decoration:none}
.news{position:absolute;left:808px;top:170px;width:266px;border-bottom:1px solid #444;padding-bottom:12px;font-size:12px;display:flex;justify-content:space-between}
.fline{position:absolute;left:105px;top:325px;width:990px;height:1px;background:#333}
.copy{position:absolute;left:153px;top:347px;font-size:11px;color:#ccc}
.fsocial{position:absolute;top:337px;width:38px;height:38px;background:#222;font-size:6px;display:flex;align-items:center;justify-content:center;color:#fff}
.totop{left:1115px;top:4158px;width:47px;height:46px;background:var(--red);display:flex;align-items:center;justify-content:center}
</style>
</head>
<body>

<!-- Top bar -->
<div class="abs topbar">
  <div class="item"><svg width="11" height="11" viewBox="0 0 24 24"><path fill="#fff" d="M6.6 10.8c1.4 2.8 3.8 5.1 6.6 6.6l2.2-2.2c.3-.3.7-.4 1-.2 1.1.4 2.3.6 3.6.6.6 0 1 .4 1 1V20c0 .6-.4 1-1 1C10.6 21 3 13.4 3 4c0-.6.4-1 1-1h3.5c.6 0 1 .4 1 1 0 1.3.2 2.5.6 3.6.1.3 0 .7-.2 1z"/></svg>Call us - (012) 555-0148</div>
  <div class="item"><svg width="12" height="10" viewBox="0 0 24 18"><rect x="1" y="1" width="22" height="16" rx="1" fill="#fff"/><path d="M1 2l11 8 11-8" stroke="#111" stroke-width="2" fill="none"/></svg>kontakt@tagfolket.example</div>
  <div class="social"><span>Friendlio</span><span>Linkora</span><span>Pictavoro</span></div>
</div>

<!-- Hero -->
<section class="abs hero" role="img" aria-label="Photo of a dark tiled pitched roof on a modern grey house under a cloudy sky">
  <div class="abs hero-shade"></div>
  <div class="abs logo" style="left:88px;top:18px">LOGO HERE</div>
  <nav class="abs nav"><span class="active">HOME</span><span>SERVICES</span><span>PROJECTS</span><span>ROOF CALCULATOR</span><span>ABOUT US</span><span>CONTACT</span></nav>
  <div class="abs btn quote-btn">Get a Free Quote</div>
  <h1 class="abs display">Your Dream Roof,<br>Our Expert Care</h1>
  <div class="abs lede">Fast, Reliable our Affordable Roofing Services — 4-5 Months me Complete</div>
  <div class="abs btn btn-est">Estimate Your Roof</div>
  <div class="abs btn btn-proj">View Our Projects</div>
</section>

<!-- Calculator -->
<section class="calc">
  <h2 class="abs display">Calculate Your<br>Roof Estimate Instantly</h2>
  <p class="abs">Use our simple roof calculator to get a quick and accurate estimate. Know your roof cost before scheduling a visit.</p>
  <div class="abs field" style="left:685px;top:882px;width:190px">Flat / Sloped / Gabled<svg width="8" height="5" viewBox="0 0 8 5"><path d="M1 1l3 3 3-3" stroke="#EB3D1F" fill="none" stroke-width="1.3"/></svg></div>
  <div class="abs field" style="left:882px;top:882px;width:190px">Enter area in sq. ft. or meters</div>
  <div class="abs field" style="left:685px;top:926px;width:190px">Tiles / Shingles / Metal<svg width="8" height="5" viewBox="0 0 8 5"><path d="M1 1l3 3 3-3" stroke="#EB3D1F" fill="none" stroke-width="1.3"/></svg></div>
  <div class="abs field" style="left:882px;top:926px;width:190px;justify-content:flex-start;gap:6px"><svg width="9" height="9"><rect x=".5" y=".5" width="8" height="8" fill="none" stroke="#EB3D1F"/></svg>Insulation, Waterproofing</div>
  <div class="abs btn calc-btn">Calculate My Roof Cost</div>
</section>

<!-- Why us -->
<section class="why">
  <div class="abs why-block"></div>
  <div class="abs why-photo" role="img" aria-label="Photo of two roofers in hard hats and safety vests laying clay tiles on a roof"></div>
  <div class="abs why-panel">
    <h2 class="display">Why Our Roofing<br>Services Are The Best</h2>
    <p>Our company has over 20 years of experience in residential and commercial roofing. We use modern techniques and high-quality materials to ensure your roof is both durable and stylish. Our team is professional, friendly, and fully insured.</p>
    <ul>
      <li><b>Fast &amp; Reliable:</b> Complete your roof in just 4-5 months</li>
      <li><b>Expert Team:</b> Skilled carpenters and roofers</li>
      <li><b>High-Quality Materials:</b> Long-lasting roofs</li>
      <li><b>Customer Satisfaction:</b> Positive reviews from satisfied clients</li>
    </ul>
  </div>
</section>

<!-- Services -->
<h2 class="abs display section-title" style="top:1722px">Our Roofing Services</h2>
<div class="abs service" style="left:0;background:linear-gradient(180deg,#a9adb2,#4b4f56 55%,#1b1c20)" role="img" aria-label="Photo of a roofer installing metal roof panels">Residential Roofing</div>
<div class="abs service" style="left:300px;background:linear-gradient(180deg,#8fa7bd,#6e6d66 55%,#2a2a2c)" role="img" aria-label="Photo of a bearded worker in a hard hat and safety vest">Commercial Roofing</div>
<div class="abs service" style="left:600px;background:linear-gradient(180deg,#2b6fc0,#a44a3a 55%,#7c1f14)" role="img" aria-label="Photo of workers repairing a gable roof">Roof Repairs &amp; Maintenance</div>
<div class="abs service" style="left:900px;background:linear-gradient(180deg,#3d4048,#2b2d33 55%,#5a4533)" role="img" aria-label="Photo of a roofer sitting on a dark metal roof">Custom Roofing Solutions</div>

<!-- Testimonials -->
<section class="testi">
  <h2 class="abs display">What Our Clients Say</h2>
  <p class="abs">Real feedback from homeowners and busi.nesses who trusted us with their roofing projects.</p>
  <div class="abs arrow-btn" style="left:222px;background:var(--ink)"><svg width="10" height="12" viewBox="0 0 10 12"><path d="M7 1L2 6l5 5" stroke="#fff" stroke-width="2" fill="none"/></svg></div>
  <div class="abs arrow-btn" style="left:277px;background:var(--red)"><svg width="10" height="12" viewBox="0 0 10 12"><path d="M3 1l5 5-5 5" stroke="#fff" stroke-width="2" fill="none"/></svg></div>
  <div class="abs review" role="img" aria-label="Faded photo of a roofer at work behind the review">
    <svg style="position:absolute;left:20px;top:52px" width="38" height="30" viewBox="0 0 38 30"><path fill="#EB3D1F" d="M0 30V17C0 7 5 2 15 0l2 5c-5 1-8 4-8 9h8v16zM21 30V17c0-10 5-15 15-17l2 5c-5 1-8 4-8 9h8v16z"/></svg>
    <div class="text">Excellent service! My new roof looks amazing and was completed quickly. The team was professional and kept me informed every step of the way.</div>
    <div class="name display">Mette L.</div>
    <div class="stars">
      <svg width="14" height="13" viewBox="0 0 24 23"><path fill="#f2a81d" d="M12 0l3.6 7.3 8 1.2-5.8 5.6 1.4 8L12 18.3 4.8 22l1.4-8L.4 8.5l8-1.2z"/></svg>
      <svg width="14" height="13" viewBox="0 0 24 23"><path fill="#f2a81d" d="M12 0l3.6 7.3 8 1.2-5.8 5.6 1.4 8L12 18.3 4.8 22l1.4-8L.4 8.5l8-1.2z"/></svg>
      <svg width="14" height="13" viewBox="0 0 24 23"><path fill="#f2a81d" d="M12 0l3.6 7.3 8 1.2-5.8 5.6 1.4 8L12 18.3 4.8 22l1.4-8L.4 8.5l8-1.2z"/></svg>
      <svg width="14" height="13" viewBox="0 0 24 23"><path fill="#f2a81d" d="M12 0l3.6 7.3 8 1.2-5.8 5.6 1.4 8L12 18.3 4.8 22l1.4-8L.4 8.5l8-1.2z"/></svg>
      <svg width="14" height="13" viewBox="0 0 24 23"><path fill="#f2a81d" d="M12 0l3.6 7.3 8 1.2-5.8 5.6 1.4 8L12 18.3 4.8 22l1.4-8L.4 8.5l8-1.2z"/></svg>
    </div>
  </div>
</section>

<!-- Projects -->
<h2 class="abs display section-title" style="top:2642px;left:35px">Our Completed Projects</h2>
<div class="abs proj" style="left:198px;top:2698px;width:397px;height:400px;background:linear-gradient(180deg,#d9dde0,#8aa27a 60%,#3f7a2f)" role="img" aria-label="Photo of a happy family walking on the lawn in front of their home"></div>
<div class="abs proj" style="left:605px;top:2698px;width:397px;height:197px;background:linear-gradient(180deg,#c9d3dd,#7c8a95 55%,#5d6b4a)" role="img" aria-label="Photo of a white two-storey house with a dark roof among trees"></div>
<div class="abs proj" style="left:605px;top:2902px;width:397px;height:196px;background:linear-gradient(180deg,#d8dde3,#9ea6ae 50%,#6e5850)" role="img" aria-label="Photo of a modern apartment building with balconies"></div>
<div class="abs proj" style="left:198px;top:3108px;width:397px;height:207px;background:linear-gradient(180deg,#8db6df,#6b6e76 55%,#2f3036)" role="img" aria-label="Photo of two roofers laying tiles on a roof"></div>
<div class="abs proj" style="left:605px;top:3108px;width:397px;height:207px;background:linear-gradient(180deg,#9cc0e3,#8a6a50 55%,#c69b6a)" role="img" aria-label="Photo of a roofer working on roof battens beside a brick chimney"></div>
<div class="abs link-badge"><svg width="26" height="26" viewBox="0 0 24 24" fill="none" stroke="#EB3D1F" stroke-width="2.4" stroke-linecap="round"><path d="M10 14a4 4 0 0 0 5.7 0l3-3a4 4 0 0 0-5.7-5.7l-1 1"/><path d="M14 10a4 4 0 0 0-5.7 0l-3 3a4 4 0 0 0 5.7 5.7l1-1"/></svg></div>

<!-- Contact -->
<section class="contact">
  <h2 class="abs display">Get In Touch With Us</h2>
  <p class="abs">Have questions or want a free quote? Contact our team and we'll guide you every step of the way.</p>
  <div class="abs ci" style="top:3615px"><svg width="20" height="20" viewBox="0 0 24 24"><path fill="#fff" d="M6.6 10.8c1.4 2.8 3.8 5.1 6.6 6.6l2.2-2.2c.3-.3.7-.4 1-.2 1.1.4 2.3.6 3.6.6.6 0 1 .4 1 1V20c0 .6-.4 1-1 1C10.6 21 3 13.4 3 4c0-.6.4-1 1-1h3.5c.6 0 1 .4 1 1 0 1.3.2 2.5.6 3.6.1.3 0 .7-.2 1z"/></svg></div>
  <div class="abs ci-label" style="top:3623px">CALL US NOW</div>
  <div class="abs ci-value" style="top:3637px">012.555.0148</div>
  <div class="abs ci" style="top:3675px"><svg width="20" height="15" viewBox="0 0 24 18"><rect x="1" y="1" width="22" height="16" rx="1" fill="#fff"/><path d="M1 2l11 8 11-8" stroke="#EB3D1F" stroke-width="2" fill="none"/></svg></div>
  <div class="abs ci-label" style="top:3683px">WRITE TO US</div>
  <div class="abs ci-value" style="top:3697px">KONTAKT@TAGFOLKET.EXAMPLE</div>
  <div class="abs form-box">
    <div class="input" style="top:45px">First Name*</div>
    <div class="input" style="top:99px">Phone Number*</div>
    <div class="input" style="top:153px">Email Address*</div>
    <div class="input" style="top:207px;height:96px">Message*</div>
    <div class="submit">Estimate Your Roof</div>
  </div>
</section>

<!-- Footer -->
<footer class="abs footer">
  <div class="flogo">LOGO HERE</div>
  <div class="fcol" style="left:373px"><h4>Quick Links</h4><a>Home</a><a>Services</a><a>Projects</a><a>Roof Calculator</a><a>About Us</a><a>Contact</a></div>
  <div class="fcol" style="left:553px"><h4>Our Services</h4><a>Residential Roofing</a><a>Commercial Roofing</a><a>Roof Repairs &amp; Maintenance</a><a>Custom Roofing Solutions</a></div>
  <div class="fcol" style="left:808px"><h4>Signup for updates on design<br>ideas and latest trends</h4></div>
  <div class="news"><span>nyt@tagfolket.example</span><svg width="12" height="12" viewBox="0 0 24 24"><path fill="#EB3D1F" d="M2 11L22 2l-9 20-2-8z"/></svg></div>
  <div class="fline"></div>
  <div class="copy">© 2025 – All Rights Reserved</div>
  <div class="fsocial" style="left:925px">Friendlio</div>
  <div class="fsocial" style="left:968px">Pictavoro</div>
  <div class="fsocial" style="left:1011px">Linkora</div>
</footer>
<div class="abs totop"><svg width="12" height="8" viewBox="0 0 12 8"><path d="M1 7l5-5 5 5" stroke="#fff" stroke-width="2" fill="none"/></svg></div>

</body>
</html>
```